Morrow Brews, alcoholic beverages with real fruit - Can Redesign

Background

Morrow Brews is a Sydney-based beverage company crafted by three long time mates. The trio decided to develop their own range of tasty, healthy alternative premix alcohol options, after seeing a huge gap in the market.

Our difference? Our beverages are crafted with premium real fruit purees that deliver unreal taste.

See website: www.morrowbrews.example
See instagram: morrow.brews

Morrow currently has 2 flavours in store - both of which have been super successful after just 5 months on shelf. The flavours:

Vodka soda lime
A mouth-watering take on an Aussie staple. Packed full of real limes (skin and all, to eliminate waste) delivering a refreshing, zesty flavour. A splash of apple juice provides natural sweetness and well rounded mouthfeel.

A highly sessionable vodka soda lime with unreal taste! Best served cold with mates.

Gin soda cucumber
The perfect combo? Our gin soda cucumber tastes just like your favourite bartender made it. Crafted with real, whole, pureed cucumbers for a refreshing, clean flavour. Balanced flawlessly with a gin featuring juniper, coriander, lemon peel, cardamom and so much more.

What is required

This brief is for the design refresh of our 2 cans.

Since launching in 2020, we have come to realise our original can designs could use a bit of an update. To customers passing by in the store, it may not be immediately obvious exactly what Morrow is. Some recent feedback on the cans included:

A customer needs to know what the product is right away when looking into fully stocked RTD/Seltzer fridges in store. The Morrow can doesn’t currently do this.
When customers glance at the can, they should be able to immediately know what the drink is, what flavour the drink is and potentially a specific USP that will make them pick up this can, over any other.

The primary objective of the can design is to get customers’ attention through hero-ing the flavour of each can on the front/side through the use of text, colour or imagery.

The specifics

The key new points that must be included on the updated can design are:

Highlight the fact our drinks use REAL FRUIT (real lime - the whole thing, and real cucumber).
This is our key USP and is why our beverages are so tasty compared to anything in stores. We want to bring this to life on our cans.
Bring to life the key flavour of each (Lime on the vodka can, Cucumber on the gin can). This could be through colour, text or imagery.
Currently, the text size and location of each flavour is quite small. And other than this text, there is no other reference to the key flavour on the can designs.

What can stay the same:

Please keep the Buff colour scheme for the vodka, and the Blue colour scheme for the gin can.
PLEASE NOTE: do not use more than 6 different colours. You pay per colour when setting up print on cans.

Please keep the MORROW logo prominent on the front of the can. Position and sizing can change.

The Morrow infographic (3 stick figures) around the neck of the can to please remain.

USPS to remain the same - the position and sizing can change:

All natural
89 calories
Low sugar

What can change:
Location of instagram handle is flexible
Infographics (Esky / Record Player) are open to interpretation. They can be kept, modified, removed or replaced.
All babydoll text to increase in size.

Please see our brand Tone of Voice and Guidelines. PLEASE NOTE the design needs to remain in our identity which can be seen on our website and instagram. We do not want a corporate style; it needs to be unique.

Files Provided:

Link to all required files: https://files.quillbox.example/receive/Kp7RtzmQxa?ref=Zq4LmN8vTyRwB2cXsD0fGhJkPoUiE3yA6tVbNmQwErTyUiOpAsDfGhJk_LzXcVb9NmQw

Target Market(s)

Males and females aged 18-40. Social, affluent, health conscious, supports local businesses, taste driven, enjoys trying new products

Font styles to use
Other font styles liked:
• Baby doll and Futura

Requirements
Must have
• A customer needs to know what the product is right away when looking into fully stocked RTD/Seltzer fridges in store. The Morrow can doesn’t currently do this.

All natural
89 calories
Low sugar
Nice to have
• A concept we are keen to explore is having the look of ripped/torn paper with the flavour exposed (e.g. green colour) underneath, see "torn paper examples" attachment for rough examples. This could be done in an illustrative style using black and buff lines on the respective cans. If this doesn't fit with your style please feel free to ignore this concept.
Should not have
• Alcohol marketing standards in Australia prevent any of the following:

show, directly imply or encourage excessive or rapid consumption of alcohol, misuse or abuse of alcohol or consumption inconsistent with the National Liquor Conduct Code

show, directly imply or encourage irresponsible or offensive alcohol related behaviour

challenge or dare people to consume an alcohol beverage

encourage choice of an alcohol beverage by emphasising its alcohol strength/intoxicating effect

have strong or evident appeal to minors

show under 25 year olds (or over 25 year olds that look like they are under 18 years of age)

suggest the consumption/presence of alcohol could contribute to a significant change in mood or environment

show or directly imply the consumption or presence of alcohol as leading to personal, business, social, sporting, sexual or other success

Imply/suggest that alcohol shown as part of a celebration is a cause of the success/ achievement

suggest the consumption of alcohol offers a therapeutic benefit or is a necessary aid to relaxation

show or directly imply the consumption of alcohol before or during any activity that for safety reasons

requires you to be alert or physically co-ordinated (i.e. driving or swimming)

```html
<!DOCTYPE html>
<html lang="en">
<head>
<meta charset="utf-8">
<title>Morrow Brews – Gin Soda Cucumber Can Label</title>
<link rel="stylesheet" href="https://fonts.googleapis.com/css2?family=Jost:wght@500;600&family=Short+Stack&display=swap">
<style>
  :root {
    --backdrop: #e4e4e4;
    --navy: #3c4053;
    --buff: #f0d2b4;
    --white: #f7f7f5;
    --leaf: #6cb13f;
    --cucumber-pale: #cfe7a6;
    --cucumber-mid: #9fcf6a;
  }
  * { box-sizing: border-box; margin: 0; padding: 0; }
  html, body {
    width: 1200px; height: 1200px; overflow: hidden;
    background: var(--backdrop);
  }
  .canvas { position: relative; width: 1200px; height: 1200px; }
  .can-label {
    position: absolute; left: 300px; top: 110px;
    width: 600px; height: 980px;
    background: var(--navy);
    overflow: hidden;
  }
  .flavour-panel { position: absolute; left: 0; top: 0; width: 600px; height: 980px; }
  .social-handle {
    position: absolute; top: 213px; width: 100%; text-align: center;
    font-family: "Short Stack", cursive; font-size: 26px; line-height: 1;
    color: var(--buff); letter-spacing: 1px;
  }
  .brand-name {
    position: absolute; top: 406px; width: 100%; text-align: center;
    font-family: "Short Stack", cursive; font-size: 76px; font-weight: 400;
    color: var(--buff); letter-spacing: 6px; line-height: 1;
  }
  .product-type {
    position: absolute; top: 556px; width: 100%; text-align: center;
    font-family: "Jost", sans-serif; font-weight: 600; font-size: 46px;
    color: var(--white); letter-spacing: 1px; line-height: 1;
  }
  .flavour-name {
    position: absolute; top: 618px; width: 100%; text-align: center;
    font-family: "Short Stack", cursive; font-size: 40px;
    color: var(--leaf); letter-spacing: 2px; line-height: 1;
  }
  .volume-info {
    position: absolute; top: 920px; width: 100%; text-align: center;
    font-family: "Jost", sans-serif; font-weight: 600; font-size: 24px; line-height: 1;
    color: var(--navy); letter-spacing: 0.5px;
  }
  .badge-text {
    font-family: "Jost", sans-serif; font-weight: 500; font-size: 16px;
    fill: var(--white); letter-spacing: 2.5px;
  }
</style>
</head>
<body>
<main class="canvas">
  <section class="can-label">
    <svg class="flavour-panel" viewBox="0 0 600 980">
      <defs>
        <linearGradient id="slice-tones" x1="0" y1="0" x2="1" y2="1">
          <stop offset="0" stop-color="#8cc653"/>
          <stop offset="1" stop-color="#6cb13f"/>
        </linearGradient>
        <path id="badge-ring" d="M242 765 a58 58 0 1 1 116 0 a58 58 0 1 1 -116 0"/>
      </defs>
      <!-- logo underline -->
      <line class="brand-underline" x1="142" y1="508" x2="462" y2="506" stroke="var(--buff)" stroke-width="9" stroke-linecap="round"/>
      <!-- torn paper edge -->
      <path d="M0 758 L30 752 L60 760 L95 750 L125 756 L150 746 L180 756 L210 770 L240 784 L262 800 L290 796 L330 770 L360 766 L392 756 L420 762 L455 748 L490 756 L520 744 L555 754 L600 746 L600 980 L0 980 Z" fill="var(--white)"/>
      <!-- exposed flavour layer -->
      <path d="M0 768 L30 762 L60 770 L95 760 L125 766 L150 756 L180 766 L210 780 L240 794 L262 810 L290 806 L330 780 L360 776 L392 766 L420 772 L455 758 L490 766 L520 754 L555 764 L600 756 L600 980 L0 980 Z" fill="url(#slice-tones)" role="img" aria-label="Illustration of fresh cucumber slices scattered across the green flavour band"/>
      <!-- real fruit badge -->
      <g class="real-fruit-badge">
        <circle cx="300" cy="765" r="74" fill="var(--navy)"/>
        <circle cx="300" cy="765" r="36" fill="var(--cucumber-pale)" role="img" aria-label="Cucumber slice illustration"/>
        <text class="badge-text"><textPath href="#badge-ring" startOffset="3%">MADE IN WITH · REAL FRUIT ·</textPath></text>
      </g>
    </svg>

    <p class="social-handle">@morrow.brews</p>
    <h1 class="brand-name">MORROW</h1>
    <p class="product-type">GIN SODA</p>
    <p class="flavour-name">cucumber</p>
    <p class="volume-info">4.2% ALC • 330 ML</p>
  </section>
</main>
</body>
</html>
```